Skin care line needs a LABEL designed!

Fernlight Skin Care... An EARTHY modern boho chic skin care line needs a label designed. It is called Fernlight because there are healing crystals in the product. Holistic, yoga feel, Earthy, feminine.

This contest is for 1 cleanser label- 2 different versions:

Gel Cleanser
Milk Cleanser

Label Size: 4.8125 x 4.8125 in

Winner will be selected to do the labels for:
Toner (5 Versions)
Serum (5 Versions)
Moisturizer (3 Versions)
Sample Label and packaging

Please be prepared to quote a price for the additional labels listed.

Inspiring Brands: **Corvella Studio**, Marigrove Organics, Tessa Wren, Halvenmoor beauty product brands,

Feel free to separate the logo symbol and use it somewhere else in the design.

Target Market(s)

Women ages 30-60

Industry/Entity Type

Skin Care Product

Requirements
Must have
• Tag Line: Inner Peace- Outer Beauty
• Area for ingredients
• Earthy feel
• Large STEP 1 on the front of packaging
• Disclaimer:
• Note: Metaphysical descriptions and healing properties of crystals are not meant to replace medical advice or treat any condition. For external use only.
Nice to have
• www.fernlight-skincare.example
Should not have
• Multiple Colors

```html
<!DOCTYPE html>
<html lang="en">
<head>
<meta charset="utf-8">
<title>Fernlight Skin Care – Gel Cleanser Label</title>
<link rel="stylesheet" href="https://fonts.googleapis.com/css2?family=Poiret+One&family=Josefin+Sans:wght@400;600&display=swap">
<style>
  :root {
    --band: #74f5e6;
    --accent: #7de8df;
    --ink: #111111;
    --paper: #ffffff;
  }
  * { margin: 0; padding: 0; box-sizing: border-box; }
  html, body { width: 1200px; height: 1200px; overflow: hidden; background: var(--paper); }
  .label {
    position: relative;
    width: 1200px;
    height: 1200px;
    background: var(--paper);
    color: var(--ink);
    font-family: "Poiret One", sans-serif;
  }
  .band {
    position: absolute;
    left: 0;
    width: 1200px;
    background: var(--band);
    display: flex;
    align-items: center;
    justify-content: center;
    font-family: "Poiret One", sans-serif;
    color: var(--ink);
  }
  .band--top { top: 0; height: 100px; }
  .band--bottom { bottom: 0; height: 101px; }
  .tagline { font-size: 72px; letter-spacing: 2px; line-height: 1; }
  .step { font-size: 112px; line-height: 1; font-weight: 400; }

  .product-name {
    position: absolute;
    left: 80px;
    top: 175px;
    width: 150px;
    height: 850px;
  }

  .brand {
    position: absolute;
    left: 300px;
    top: 165px;
    width: 500px;
    text-align: center;
    color: var(--accent);
    font-family: "Poiret One", sans-serif;
    font-weight: 400;
  }
  .brand__name { display: block; font-size: 104px; line-height: 1; }
  .brand__sub { display: block; font-size: 60px; line-height: 1.1; }

  .emblem {
    position: absolute;
    left: 395px;
    top: 395px;
    width: 366px;
    height: 366px;
    border-radius: 50%;
    background: var(--accent);
  }

  .claim {
    position: absolute;
    left: 300px;
    top: 780px;
    width: 530px;
    text-align: center;
    font-size: 48px;
    line-height: 64px;
  }

  .info {
    position: absolute;
    font-family: "Poiret One", sans-serif;
    color: var(--ink);
  }
  .info strong { font-family: "Josefin Sans", sans-serif; font-weight: 600; }
  .directions { left: 821px; top: 152px; width: 360px; font-size: 30px; line-height: 37px; }
  .ingredients { left: 825px; top: 280px; font-size: 29px; }
  .note { left: 839px; top: 655px; width: 340px; font-size: 22px; line-height: 29px; }
  .note strong { font-size: 21px; }
  .disclaimer { left: 835px; top: 866px; font-size: 21px; }
</style>
</head>
<body>
  <main class="label">
    <header class="band band--top">
      <p class="tagline">Inner Peace-Outer Beauty</p>
    </header>

    <svg class="product-name" viewBox="0 0 150 850" aria-label="Gel Cleanser">
      <text x="-425" y="132" transform="rotate(-90)" text-anchor="middle"
            textLength="830" lengthAdjust="spacingAndGlyphs"
            font-family="Poiret One, sans-serif" font-size="185" fill="#111111">GEL CLEANSER</text>
    </svg>

    <div class="brand">
      <span class="brand__name">Fernlight</span>
      <span class="brand__sub">Skin Care</span>
    </div>

    <div class="emblem" role="img" aria-label="Lotus mandala ornament in aqua"></div>

    <p class="claim">Our natural<br>oils melt away<br>make-up and impurities</p>

    <p class="info directions"><strong>Directions:</strong> Massage onto skin- rinse.</p>
    <p class="info ingredients"><strong>Ingredients:</strong></p>
    <p class="info note"><strong>Note:</strong> Metaphysical descriptions and healing properties of crystals are not meant to replace medical advice or treatment any condition. For external use only.</p>
    <p class="info disclaimer"><strong>Disclaimer:</strong></p>

    <footer class="band band--bottom">
      <p class="step">Step 1</p>
    </footer>
  </main>
</body>
</html>
```